Business Card Design

Carl Benson Insurance Agency, an Independent Insurance Agency which was stated on Orchard Lane in Laplace, Louisiana on 1958 and has grown the six locations throughout South Louisiana. We sell personal (auto Homeowners flood, liability) and commercial insurance (commercial property, general liability, workers compensation, commercial auto). I am looking for a double sided card with list the five remaining locations on the back or maybe even a folded four sided card. Our home office is a two story building with a green roof. I have had a logo designed which I have attached. Open for revisions but would like to stay with in the same green roof over an M. I have attached the logo but can not tell if I was uploaded.

Target Market(s)

Individual and commercial insurance buyers. Upper income and business owners

Industry/Entity Type

Insurance

Requirements
Must have
• Must have similar logo as uploaded. Green roof over M or something similar. List all location address and phone numbers.

Employee name, office phone number; direct phone line; email address and website list all locations on card. Very Similar colors to current logo.
Nice to have
• Possible folded card with double sided print

```html
<!DOCTYPE html>
<html lang="en">
<head>
<meta charset="utf-8">
<title>Carl Benson Insurance Agency – Business Card</title>
<link rel="stylesheet" href="https://fonts.googleapis.com/css2?family=Roboto+Condensed:wght@400;700&display=swap">
<style>
  :root {
    --green: #1f7a4f;
    --blue: #1f7fc4;
    --blue-light: #3aa0d8;
    --blue-dark: #155f9e;
    --grey: #7d8a8f;
    --text-dark: #2b3a3f;
    --paper: #ffffff;
    --backdrop: #e9e7e2;
  }
  * { margin: 0; padding: 0; box-sizing: border-box; }
  html, body {
    width: 1200px; height: 858px; overflow: hidden;
    background: var(--backdrop);
    font-family: "Roboto Condensed", "Arial Narrow", sans-serif;
  }
  .canvas {
    position: relative; width: 1200px; height: 858px;
    display: flex; align-items: center; justify-content: center; gap: 40px;
  }
  .card {
    position: relative; width: 560px; height: 320px;
    background: var(--paper); overflow: hidden;
    box-shadow: 0 6px 18px rgba(0,0,0,0.15);
  }
  /* Front */
  .card-wave { position: absolute; inset: 0; width: 100%; height: 100%; }
  .brand {
    position: absolute; left: 70px; top: 46px;
    display: flex; align-items: flex-start; gap: 12px;
  }
  .brand-mark { width: 24px; height: 24px; background: var(--green); margin-top: 6px; flex: none; }
  .brand-name {
    color: var(--green); font-weight: 700; text-transform: uppercase;
    font-size: 28px; line-height: 1.02; letter-spacing: 0.3px;
  }
  .brand-tagline {
    margin-top: 6px; color: var(--grey); font-weight: 700; font-size: 15px;
  }
  .contact-list {
    position: absolute; right: 30px; top: 150px; list-style: none;
    display: flex; flex-direction: column; gap: 7px; align-items: flex-end;
  }
  .contact-item {
    display: flex; align-items: center; gap: 10px;
    color: var(--text-dark); font-size: 15px; line-height: 18px;
  }
  .contact-icon { width: 16px; height: 16px; flex: none; }
  .employee-name {
    position: absolute; left: 34px; bottom: 26px;
    color: #fff; font-weight: 700; font-size: 22px;
  }
  /* Back */
  .card-back { display: flex; align-items: center; justify-content: center; }
  .back-lockup { text-align: left; }
  .back-name {
    color: var(--green); font-weight: 700; text-transform: uppercase; line-height: 0.98;
  }
  .back-name .line-1 { display: block; font-size: 64px; }
  .back-name .line-2 { display: block; font-size: 38px; letter-spacing: 0.5px; }
  .back-tagline { margin-top: 8px; color: var(--grey); font-weight: 700; font-size: 24px; }
</style>
</head>
<body>
<main class="canvas">

  <section class="card card-front" aria-label="Card front">
    <svg class="card-wave" viewBox="0 0 560 320" preserveAspectRatio="none" aria-hidden="true">
      <defs>
        <linearGradient id="waveBlue" x1="0" y1="0" x2="1" y2="1">
          <stop offset="0" stop-color="#155f9e"/>
          <stop offset="0.55" stop-color="#3aa0d8"/>
          <stop offset="1" stop-color="#1f7fc4"/>
        </linearGradient>
      </defs>
      <path d="M0,166 C150,230 340,262 548,262 C340,268 150,245 0,182 Z" fill="#1f7a4f"/>
      <path d="M0,192 C150,252 340,280 560,272 L560,320 L0,320 Z" fill="url(#waveBlue)"/>
    </svg>

    <div class="brand">
      <span class="brand-mark" aria-hidden="true"></span>
      <div>
        <div class="brand-name">Carl Benson<br>Insurance Agency</div>
        <div class="brand-tagline">Serving Orchard Lane Since 1958</div>
      </div>
    </div>

    <ul class="contact-list">
      <li class="contact-item">xxx xxxx xxxx
        <svg class="contact-icon" viewBox="0 0 16 16" aria-hidden="true"><rect width="16" height="16" rx="3" fill="#1f7fc4"/><path d="M4 4.5c0 4 3.5 7.5 7.5 7.5l.8-1.8-2-1-1 1c-1.2-.6-2.4-1.8-3-3l1-1-1-2z" fill="#fff"/></svg>
      </li>
      <li class="contact-item">xxx xxxx xxxx
        <svg class="contact-icon" viewBox="0 0 16 16" aria-hidden="true"><rect x="3.5" y="1" width="9" height="14" rx="1.5" fill="none" stroke="#1f7fc4" stroke-width="1.6"/><circle cx="8" cy="12.5" r="0.9" fill="#1f7fc4"/></svg>
      </li>
      <li class="contact-item">info@youremail.com
        <svg class="contact-icon" viewBox="0 0 16 16" aria-hidden="true"><rect y="3" width="16" height="10" rx="1" fill="#1f7fc4"/><path d="M1 4l7 5 7-5M1 12l5-4M15 12l-5-4" stroke="#fff" stroke-width="1.2" fill="none"/></svg>
      </li>
      <li class="contact-item">www.yourwebsite.com
        <svg class="contact-icon" viewBox="0 0 16 16" aria-hidden="true"><circle cx="8" cy="8" r="7" fill="#1f7fc4"/><path d="M1 8h14M8 1c-3 3.5-3 10.5 0 14M8 1c3 3.5 3 10.5 0 14" stroke="#fff" stroke-width="1" fill="none"/></svg>
      </li>
    </ul>

    <div class="employee-name">Employee Name</div>
  </section>

  <section class="card card-back" aria-label="Card back">
    <div class="back-lockup">
      <div class="back-name">
        <span class="line-1">Carl Benson</span>
        <span class="line-2">Insurance Agency</span>
      </div>
      <div class="back-tagline">Serving Orchard Lane Since 1958</div>
    </div>
  </section>

</main>
</body>
</html>
```